Adorable Luxury Flower Shop

Need a beautiful, eye catching, elegant full-service website.
INSPIRATIONS ARE;
https://www.quillmoreblooms.com

Industry/Entity Type

retail, floral, boutique

Coding

Coded - Design and coding required

Number of Pages Required

3 page

Requirements
Must have
• SEO, Coded, UX, Fully responsive mobile, tablet, desktop, Ecommerce setup with Square, payments integration (if we use squarespace). SEO optimization with keywords, tags, meta descriptions, Load speed optimization, Google my business setup.
Nice to have
• pictures, color, elegance

```html
<!DOCTYPE html>
<html lang="en">
<head>
<meta charset="utf-8">
<title>Maribelle Flower Boutique</title>
<link href="https://fonts.googleapis.com/css2?family=Cormorant+Garamond:ital,wght@0,500;0,600;0,700;1,600;1,700&family=Jost:wght@400;500&family=Marcellus&display=swap" rel="stylesheet">
<style>
:root{
  --red:#c41a1f;
  --ink:#1b1b1b;
  --muted:#444;
  --line:#d9d9d9;
  --soft:#f1eff0;
  --card:#f2f2f2;
  --dark:#222222;
}
*{box-sizing:border-box;margin:0;padding:0}
html,body{width:1200px;height:4754px;overflow:hidden}
body{position:relative;background:#fff;font-family:'Jost',sans-serif;color:var(--ink)}
.abs{position:absolute}
.serif{font-family:'Cormorant Garamond',serif}
a{color:inherit;text-decoration:none}

/* header */
.site-header{position:absolute;left:0;top:0;width:1200px;height:120px;background:#fff}
.brand{position:absolute;left:68px;top:40px;display:flex;align-items:center;gap:10px;font-family:'Cormorant Garamond',serif;font-weight:700;font-size:34px;color:var(--ink)}
.brand-dot{width:18px;height:18px;border-radius:50%;background:var(--red)}
.main-nav{position:absolute;top:56px;left:374px;display:flex;gap:38px;font-size:15px}
.main-nav a.active{color:var(--red);border-bottom:2px solid var(--red);padding-bottom:8px}
.header-icons{position:absolute;top:48px;left:986px;display:flex;gap:22px}

/* hero */
.hero{position:absolute;left:0;top:120px;width:1200px;height:740px;
  background:radial-gradient(ellipse 420px 340px at 860px 330px,#b8141b 0%,#d23a3e 40%,#eee4e2 75%,transparent 100%),linear-gradient(90deg,#eaeaea 0%,#dedede 50%,#e8e6e4 100%)}
.hero-title{position:absolute;left:68px;top:150px;font-family:'Marcellus',serif;font-size:42px;line-height:62px;letter-spacing:1px;color:var(--ink)}
.btn{display:inline-flex;align-items:center;justify-content:center;border-radius:30px;color:#fff;font-size:18px}
.btn-red{background:var(--red)}
.hero .btn{position:absolute;left:68px;top:390px;width:186px;height:56px}

/* section titles */
.section-title{position:absolute;left:0;width:1200px;text-align:center;font-family:'Cormorant Garamond',serif;font-weight:500;font-size:46px;color:var(--ink)}
.section-title span::before,.section-title span::after{content:"";display:inline-block;width:38px;height:2px;background:var(--red);vertical-align:middle;margin:0 12px}
.section-lead{position:absolute;left:120px;width:960px;text-align:center;font-size:15px;line-height:24px;color:var(--ink)}

/* products */
.product{position:absolute;width:256px;height:421px;border:1px solid var(--line);background:#fff;text-align:center}
.product .photo{position:absolute;left:22px;top:14px;width:212px;height:218px;border-radius:4px}
.product h3{position:absolute;top:262px;width:100%;font-weight:500;font-size:19px}
.product p{position:absolute;top:290px;width:100%;font-size:11.5px}
.product .price{position:absolute;top:318px;width:100%;font-size:24px;font-weight:500}
.product .pill{position:absolute;left:82px;top:366px;width:92px;height:30px;border:1.5px solid var(--red);border-radius:16px;font-size:12px;line-height:27px}
.ph-pink{background:radial-gradient(circle at 50% 45%,#e0499a,#f0a6cf 55%,#fff 80%)}
.ph-lilac{background:radial-gradient(circle at 50% 45%,#b994b4,#e6d2e0 55%,#fff 80%)}
.ph-yellow{background:radial-gradient(circle at 50% 42%,#f2b619,#f7dc7a 45%,#fff 75%)}
.ph-rose{background:radial-gradient(circle at 50% 40%,#d1124e,#eb6f95 45%,#fff 75%)}
.btn-dark{position:absolute;left:507px;top:2066px;width:186px;height:56px;background:#111;color:#fff;border-radius:30px;font-size:18px;display:flex;align-items:center;justify-content:center}

/* features */
.feature{position:absolute;top:2234px;width:330px;height:106px;background:var(--card);border:1px solid #b9b9b9;display:flex;align-items:center;gap:22px;padding-left:34px;font-size:19px}

/* offer */
.offer{position:absolute;left:68px;top:2485px;width:1068px;height:553px;border-radius:30px;background:#f3f2f4;overflow:hidden;box-shadow:2px 2px 4px rgba(0,0,0,.12)}
.offer .photo{position:absolute;left:0;top:0;width:590px;height:553px;background:radial-gradient(ellipse at 55% 55%,#fbf7ee 0%,#f1c9cf 35%,#c9d7a8 60%,#f3f2f4 85%)}
.offer .frame{position:absolute;left:16px;top:24px;width:1030px;height:505px;border:2px dotted var(--red);border-radius:20px;clip-path:polygon(0 55%,0 100%,50% 100%,50% 95%,60% 0,100% 0,100% 40%,60% 0,0 0)}
.offer .text{position:absolute;left:560px;width:440px;text-align:center}
.special{top:80px;font-family:'Cormorant Garamond',serif;font-style:italic;font-weight:700;font-size:44px;color:var(--red)}
.summer{top:128px;font-family:'Cormorant Garamond',serif;font-weight:600;font-size:110px;line-height:110px;letter-spacing:2px}
.sale{top:234px;font-family:'Cormorant Garamond',serif;font-style:italic;font-weight:700;font-size:58px}
.upto{top:300px;font-size:56px;font-weight:500}
.offer .btn{position:absolute;left:697px;top:433px;width:186px;height:56px}

/* reviews */
.review{position:absolute;top:3323px;width:292px;height:210px;background:#fff;box-shadow:0 2px 10px rgba(0,0,0,.12);border-bottom:5px solid var(--red);padding:22px 24px}
.review .avatar{position:absolute;left:20px;top:18px;width:56px;height:56px;border-radius:50%;background:linear-gradient(135deg,#c9b6a3,#6b5548)}
.review h4{position:absolute;left:92px;top:26px;font-weight:500;font-size:14px}
.review .stars{position:absolute;left:92px;top:46px;font-size:9px;color:#e2b100;letter-spacing:1px}
.review .quote{position:absolute;right:22px;top:40px;font-family:'Cormorant Garamond',serif;font-size:54px;color:#ddd;line-height:1}
.review p{position:absolute;left:24px;top:102px;width:240px;font-size:12px;line-height:21px;color:var(--muted)}
.arrow{position:absolute;width:40px;height:40px;border-radius:50%;display:flex;align-items:center;justify-content:center;font-size:14px}

/* instagram */
.insta{position:absolute;left:0;top:3600px;width:1200px;height:618px;background:var(--soft)}
.insta-photo{position:absolute;top:190px;height:273px}

/* newsletter */
.subscribe{position:absolute;left:208px;top:4390px;width:784px;height:72px;border:1.5px solid #777;border-radius:36px;font-size:14px;padding-left:28px;line-height:70px}
.subscribe .btn{position:absolute;right:10px;top:14px;width:142px;height:42px;font-size:15px}

/* footer */
.site-footer{position:absolute;left:0;top:4521px;width:1200px;height:233px;background:var(--dark);color:#fff}
.footer-rule{position:absolute;left:68px;width:1064px;height:1px;background:#666}
.footer-nav{position:absolute;top:114px;display:flex;gap:40px;font-size:15px}
.footer-brand{position:absolute;left:470px;top:60px;width:260px;height:110px;background:var(--dark);display:flex;align-items:center;justify-content:center;gap:10px;font-family:'Cormorant Garamond',serif;font-weight:700;font-size:38px;color:#fff}
.social{position:absolute;left:768px;top:165px;display:flex;gap:14px}
.social i{width:14px;height:14px;border-radius:50%;background:#fff;display:block}
.cards{position:absolute;left:914px;top:165px;display:flex;gap:6px}
.cards i{width:22px;height:14px;border-radius:2px;background:#8f8f8f;display:block}
.copyright{position:absolute;left:68px;top:190px;font-size:11px}
</style>
</head>
<body>

<header class="site-header">
  <div class="brand"><span class="brand-dot"></span>Maribelle</div>
  <nav class="main-nav">
    <a class="active" href="#">Home</a><a href="#">Shop</a><a href="#">About Us</a><a href="#">Blogs</a><a href="#">Pages</a><a href="#">Contact Us</a>
  </nav>
  <div class="header-icons">
    <svg width="34" height="34" viewBox="0 0 34 34" fill="none" stroke="#111" stroke-width="2.4"><circle cx="14" cy="14" r="11"/><path d="M22 22l10 10"/></svg>
    <svg width="34" height="34" viewBox="0 0 34 34" fill="none" stroke="#111" stroke-width="2.4"><circle cx="17" cy="17" r="15"/><circle cx="17" cy="13" r="5"/><path d="M7 28c3-6 17-6 20 0"/></svg>
    <svg width="28" height="34" viewBox="0 0 28 34" fill="none" stroke="#111" stroke-width="2.4"><rect x="2" y="10" width="24" height="22" rx="2"/><path d="M8 14V8a6 6 0 0112 0v6"/></svg>
  </div>
</header>

<section class="hero" role="img" aria-label="Bouquet of red and white roses in a glass vase against a soft window light">
  <h1 class="hero-title">Bring the Outdoors In<br>with our Beautiful<br>Flowers</h1>
  <a class="btn btn-red" href="#">Shop Now</a>
</section>

<h2 class="section-title" style="top:946px"><span>Fresh Picks</span></h2>
<p class="section-lead" style="top:1020px">Lorem ipsum dolor sit amet, consectetur adipiscing elit, sed do eiusmod tempor incididunt ut labore et dolore magna aliqua. Quis ipsum suspendisse ultrices gravida. Risus commodo viverra maecenas accumsan lacus vel facilisis.</p>

<div class="product" style="left:68px;top:1143px"><div class="photo ph-pink" role="img" aria-label="Pink lily bouquet"></div><h3>Lily Lane</h3><p>Lorem ipsum dolor sit amet, cons</p><div class="price">$40.00</div><a class="pill" href="#">Shop Now</a></div>
<div class="product" style="left:336px;top:1143px"><div class="photo ph-lilac" role="img" aria-label="Lilac and white lily bouquet"></div><h3>Daisy Dreams</h3><p>Lorem ipsum dolor sit amet, cons</p><div class="price">$30.00</div><a class="pill" href="#">Shop Now</a></div>
<div class="product" style="left:604px;top:1143px"><div class="photo ph-yellow" role="img" aria-label="Yellow tulips in a glass vase"></div><h3>Rose Varities</h3><p>Lorem ipsum dolor sit amet, cons</p><div class="price">$20.00</div><a class="pill" href="#">Shop Now</a></div>
<div class="product" style="left:872px;top:1143px"><div class="photo ph-rose" role="img" aria-label="Bouquet of magenta roses"></div><h3>Rose Bloom</h3><p>Lorem ipsum dolor sit amet, cons</p><div class="price">$30.00</div><a class="pill" href="#">Shop Now</a></div>

<div class="product" style="left:68px;top:1603px"><div class="photo ph-pink" role="img" aria-label="Pink lily bouquet"></div><h3>Lily Lane</h3><p>Lorem ipsum dolor sit amet, cons</p><div class="price">$40.00</div><a class="pill" href="#">Shop Now</a></div>
<div class="product" style="left:336px;top:1603px"><div class="photo ph-lilac" role="img" aria-label="Lilac and white lily bouquet"></div><h3>Daisy Dreams</h3><p>Lorem ipsum dolor sit amet, cons</p><div class="price">$30.00</div><a class="pill" href="#">Shop Now</a></div>
<div class="product" style="left:604px;top:1603px"><div class="photo ph-yellow" role="img" aria-label="Yellow tulips in a glass vase"></div><h3>Rose Varities</h3><p>Lorem ipsum dolor sit amet, cons</p><div class="price">$20.00</div><a class="pill" href="#">Shop Now</a></div>
<div class="product" style="left:872px;top:1603px"><div class="photo ph-rose" role="img" aria-label="Bouquet of magenta roses"></div><h3>Rose Bloom</h3><p>Lorem ipsum dolor sit amet, cons</p><div class="price">$30.00</div><a class="pill" href="#">Shop Now</a></div>

<a class="btn-dark" href="#">View All</a>

<div class="feature" style="left:68px">
  <svg width="76" height="60" viewBox="0 0 76 60" fill="none" stroke="#c41a1f" stroke-width="2.4"><rect x="2" y="16" width="46" height="30" rx="3"/><path d="M48 24h14l10 12v10H48"/><circle cx="16" cy="50" r="6"/><circle cx="60" cy="50" r="6"/><rect x="14" y="4" width="18" height="12"/><path d="M23 4v12"/></svg>
  <span>Free Shipping</span>
</div>
<div class="feature" style="left:436px">
  <svg width="76" height="60" viewBox="0 0 76 60" fill="none" stroke="#c41a1f" stroke-width="2.4"><rect x="4" y="12" width="68" height="40" rx="4"/><path d="M26 12v40M4 30h22"/><path d="M18 12c-6-10 8-10 8 0c0-10 14-10 8 0"/><circle cx="54" cy="34" r="8"/></svg>
  <span>Offer and Gift</span>
</div>
<div class="feature" style="left:804px">
  <svg width="76" height="60" viewBox="0 0 76 60" fill="none" stroke="#c41a1f" stroke-width="2.4"><path d="M38 4l12 5v9c0 8-6 12-12 14c-6-2-12-6-12-14V9z"/><path d="M32 17l5 5l8-8"/><path d="M6 38l14-6l12 8l10-6l14 4l14 6M20 32l16 20l14-10"/></svg>
  <span>Reliability</span>
</div>

<section class="offer">
  <div class="photo" role="img" aria-label="Bouquet of white peonies and pink blooms wrapped in kraft paper"></div>
  <div class="frame"></div>
  <div class="text special abs">SPECIAL OFFER</div>
  <div class="text summer abs">SUMMER</div>
  <div class="text sale abs">Sale</div>
  <div class="text upto abs">UP TO 50% OFF</div>
  <a class="btn btn-red" href="#">Shop Now</a>
</section>

<h2 class="section-title" style="top:3128px"><span>Client Reviews</span></h2>
<p class="section-lead" style="top:3215px">Lorem ipsum dolor sit amet, consectetur adipiscing elit, sed do eiusmod tempor incididunt ut labore et dolore magna aliqua. Quis ipsum suspendisse ultrices gravida. Risus commodo viverra maecenas accumsan lacus vel facilisis.</p>

<div class="arrow" style="left:55px;top:3384px;background:#f4d5d8;color:#c41a1f">&#8249;</div>
<div class="review" style="left:143px"><div class="avatar" role="img" aria-label="Reviewer portrait"></div><h4>Elias Morrow</h4><div class="stars">★★★★★</div><div class="quote">”</div><p>Lorem ipsum dolor sit amet, consect etur adipiscing elit, sed do eiusmod tempor incididunt ut labore et</p></div>
<div class="review" style="left:459px"><div class="avatar" role="img" aria-label="Reviewer portrait"></div><h4>Elias Morrow</h4><div class="stars">★★★★★</div><div class="quote">”</div><p>Lorem ipsum dolor sit amet, consect etur adipiscing elit, sed do eiusmod tempor incididunt ut labore et</p></div>
<div class="review" style="left:775px"><div class="avatar" role="img" aria-label="Reviewer portrait"></div><h4>Elias Morrow</h4><div class="stars">★★★★★</div><div class="quote">”</div><p>Lorem ipsum dolor sit amet, consect etur adipiscing elit, sed do eiusmod tempor incididunt ut labore et</p></div>
<div class="arrow" style="left:1116px;top:3384px;background:#c41a1f;color:#fff">&#8250;</div>

<section class="insta">
  <h2 class="section-title" style="top:72px"><span>Follow Us On Instagram</span></h2>
  <div class="insta-photo" style="left:68px;width:272px;background:radial-gradient(circle at 50% 50%,#c8223a,#e8e2cf 55%,#d8c8b4)" role="img" aria-label="Red and cream rose bouquet"></div>
  <div class="insta-photo" style="left:357px;width:272px;background:linear-gradient(160deg,#f08cb4,#f8c7da 60%,#f6dde6)" role="img" aria-label="Pink gerbera in a vase on pink backdrop"></div>
  <div class="insta-photo" style="left:649px;width:266px;background:radial-gradient(circle at 50% 40%,#e24a5a,#9fb2c4 65%,#6f8aa2)" role="img" aria-label="Pink roses in a glass vase by the water"></div>
  <div class="insta-photo" style="left:932px;width:268px;background:radial-gradient(circle at 40% 60%,#d767a8,#eee6e8 60%,#f2ede9)" role="img" aria-label="Pink and purple bouquet on a white sofa"></div>
  <div class="arrow" style="left:1113px;top:310px;background:#111;color:#fff">&#8250;</div>
</section>

<h2 class="section-title" style="top:4266px"><span>Subscribe to our newsletter</span></h2>
<p class="section-lead" style="top:4336px">Sign up for our newsletter to hear about our Deals of the Week, special sales and more.</p>
<div class="subscribe">Enter Your Email Address<a class="btn btn-red" href="#">SUBSCRIBE</a></div>

<footer class="site-footer">
  <div class="footer-rule" style="top:80px"></div>
  <div class="footer-rule" style="top:156px"></div>
  <nav class="footer-nav" style="left:178px"><a href="#">Home</a><a href="#">Shop</a><a href="#">About Us</a></nav>
  <nav class="footer-nav" style="left:784px"><a href="#">Blogs</a><a href="#">Pages</a><a href="#">Contact Us</a></nav>
  <div class="footer-brand"><span class="brand-dot"></span>Maribelle</div>
  <div class="social"><i></i><i></i><i></i><i></i></div>
  <div class="cards"><i></i><i></i><i></i><i></i><i></i><i></i><i></i><i></i><i></i></div>
  <div class="copyright">Copyright © 2025 All Rights Reserved By Company name</div>
</footer>

</body>
</html>
```